Emerging Australian photographer

I'm based in Cunderdin, a small rural town in the Wheatbelt area of Western Australia. So its a good thing that I love to travel further afield both for pleasure and for work. To me that is one and the same thing in any event!

My desire is to take photos that make the viewers heart skip. I love taking photos of people doing the things they love or being with the people they love. For me, the joy of photography comes with capturing the 'moments between the moments'. I like candid photography best of all - like when the new husband is staring joyfully at his bride and at that minute is unaware of the photographer capturing the moment.

I am available for weddings, engagements, birthdays, special events, newborns, family or individual portraits. By the end of the year I will be accredited with the Southern Guild of Practising Imagemakers.

I need a card that stands out but is elegant and would sit well on the table at a wedding or be given out in the church grounds. Classy and a little bit sassy.

Target Market(s)

Consumers who are seeking photographic services, eg wedding guests who see me at work and make enquiries.

Industry/Entity Type

Church

Contact Information for Business Card

Danielle Whitcombe Photography
Danielle Whitcombe
0438 562 073
www.daniellewhitcombe.com.au
photos@daniellewhitcombe.com.au

Requirements
Must have
• Must fit with the theme in the watermarks, but be crisp and modern.
Nice to have
• However it's not essential to have the pink! Chatterbook and Pipsqueak logos.
Should not have
• Old style fonts like times new roman.

```html
<!DOCTYPE html>
<html lang="en">
<head>
<meta charset="utf-8">
<title>Danielle Whitcombe Photography – Business Card</title>
<link rel="stylesheet" href="https://fonts.googleapis.com/css2?family=Poiret+One&family=Quicksand:wght@400;500&display=swap">
<style>
  :root {
    --backdrop: #e9e6e1;
    --card-core: #5d5e62;
    --card-edge: #2f3033;
    --ink: #f4f4f4;
    --ink-soft: #d9d9db;
    --ink-faint: rgba(255, 255, 255, 0.14);
    --icon-fill: #8a8a8c;
    --accent-pink: #e7a9c2;
  }
  * { margin: 0; padding: 0; box-sizing: border-box; }
  html, body {
    width: 1200px; height: 1000px; overflow: hidden;
    background: var(--backdrop);
  }
  .stage {
    position: relative; width: 1200px; height: 1000px;
  }
  .card {
    position: absolute;
    background: radial-gradient(ellipse at 50% 45%, var(--card-core) 0%, #48494c 45%, var(--card-edge) 100%);
    box-shadow: 0 10px 28px rgba(0, 0, 0, 0.22);
    color: var(--ink);
    font-family: "Poiret One", "Quicksand", sans-serif;
    overflow: hidden;
  }

  /* Front – portrait contact side */
  .card-front {
    left: 110px; top: 200px; width: 350px; height: 600px;
  }
  .front-heading {
    position: absolute; top: 52px; right: 34px; text-align: right;
  }
  .front-name {
    font-size: 36px; letter-spacing: 0.5px; line-height: 1;
  }
  .front-trade {
    margin-top: 4px; font-size: 12px; letter-spacing: 5px;
    color: var(--ink-soft); margin-right: -5px;
  }
  .front-contact {
    position: absolute; top: 210px; left: 0; right: 0; text-align: center;
  }
  .contact-phone { font-size: 20px; letter-spacing: 1px; }
  .contact-email { font-size: 17px; margin-top: 6px; }
  .contact-web { font-size: 11px; margin-top: 6px; color: var(--ink-soft); letter-spacing: 0.5px; }
  .social-list {
    display: flex; justify-content: center; gap: 18px; margin-top: 18px;
    font-family: "Quicksand", sans-serif; font-size: 11px; color: var(--ink-soft);
  }
  .social-item { display: flex; align-items: center; gap: 6px; }
  .social-square {
    width: 14px; height: 14px; border-radius: 3px; background: var(--icon-fill);
  }
  .front-watermark {
    position: absolute; left: -10px; bottom: 70px; width: 380px;
    text-align: center; font-size: 46px; line-height: 1.05;
    color: var(--ink-faint);
  }

  /* Back – landscape brand side */
  .card-back {
    left: 530px; top: 325px; width: 600px; height: 350px;
  }
  .back-brand {
    position: absolute; inset: 0;
    display: flex; align-items: center; justify-content: center; gap: 14px;
  }
  .brand-dot {
    width: 12px; height: 12px; border-radius: 50%; background: var(--accent-pink);
  }
  .brand-name {
    font-size: 34px; letter-spacing: 1px; color: var(--ink);
  }
</style>
</head>
<body>
<main class="stage">

  <section class="card card-front" aria-label="Business card front">
    <header class="front-heading">
      <h1 class="front-name">Danielle Whitcombe</h1>
      <p class="front-trade">Photography</p>
    </header>

    <div class="front-contact">
      <p class="contact-phone">0438 562 073</p>
      <p class="contact-email">photos@daniellewhitcombe.com.au</p>
      <p class="contact-web">www.daniellewhitcombe.com.au</p>
      <ul class="social-list">
        <li class="social-item"><span class="social-square"></span>Pipsqueak</li>
        <li class="social-item"><span class="social-square"></span>Chatterbook</li>
      </ul>
    </div>

    <p class="front-watermark" aria-hidden="true">Danielle Whitcombe</p>
  </section>

  <section class="card card-back" aria-label="Business card back">
    <div class="back-brand">
      <span class="brand-dot"></span>
      <p class="brand-name">Danielle Whitcombe Photography</p>
    </div>
  </section>

</main>
</body>
</html>
```